Copper Brook Estate

We are a prestigeous estate offering horse boarding and training in Dressage, Western and more. Offering the newest technology, ZELTA, for remote trainers and their students. Will need links to Facebook and Instagram sites. Drop down menus for services offered. Logo has already been created along with a marketing flier which is attached. Other photos will be loaded onto a zip file.
Other amenities to highlight:
200x60 covered and lighted arena.
2 additional outdoor arenas
Hot/cold water wash rack
Live-in manager
Specialized care for your horses
All levels of riders welcome

Thank you for the current submissions! Please keep them coming!

```html
<!DOCTYPE html>
<html lang="en">
<head>
<meta charset="utf-8">
<title>Copper Brook Stables</title>
<link href="https://fonts.googleapis.com/css2?family=Montserrat:wght@400;500;600;700&family=Raleway:wght@400;500&display=swap" rel="stylesheet">
<style>
:root{
  --olive:#7a7228;
  --olive-dark:#5f5a1e;
  --cream:#f8f7f0;
  --white:#ffffff;
  --ink:#3b3a30;
  --muted:#6d6b5a;
}
*{box-sizing:border-box;margin:0;padding:0}
html,body{width:1200px;height:3124px;overflow:hidden}
body{position:relative;background:var(--cream);font-family:"Raleway",sans-serif;color:var(--ink)}
a{text-decoration:none}
.abs{position:absolute}
.hero{left:0;top:0;width:1200px;height:472px;background:linear-gradient(100deg,#1f1a14 0%,#3a2f22 45%,#5a4a36 75%,#2a231a 100%)}
.brand{left:40px;top:22px;display:flex;align-items:center;gap:10px;color:var(--white);font-family:"Montserrat",sans-serif;font-weight:600;font-size:13px;letter-spacing:2px}
.brand-dot{width:26px;height:26px;border:2px solid var(--white);border-radius:50%}
.nav{right:60px;top:28px;display:flex;gap:4px}
.nav a{font-family:"Montserrat",sans-serif;font-size:11px;font-weight:600;letter-spacing:1px;color:var(--white);padding:6px 18px}
.nav a.active{background:var(--olive)}
.hero-title{left:280px;top:148px;font-family:"Montserrat",sans-serif;font-weight:700;font-size:50px;line-height:1.1;color:var(--white);letter-spacing:1px}
.hero-sub{left:282px;top:282px;font-size:15px;color:var(--white)}
.btn{display:inline-block;background:var(--olive);color:var(--white);font-family:"Montserrat",sans-serif;font-weight:600;font-size:12px;letter-spacing:1.5px;padding:10px 26px}
.hero-btn{left:282px;top:326px}
.hero-tag{left:282px;top:394px;font-family:"Montserrat",sans-serif;font-weight:600;font-size:17px;color:var(--white);letter-spacing:1px}

.welcome{left:0;top:496px;width:1200px;text-align:center}
.welcome h2{font-family:"Montserrat",sans-serif;font-weight:700;font-size:22px;color:var(--olive);letter-spacing:1px}
.welcome p{font-family:"Montserrat",sans-serif;font-size:14px;color:var(--olive);margin-top:4px;letter-spacing:1px}
.facility{left:200px;top:570px;width:860px;display:flex;gap:60px}
.facility ul{flex:1;list-style:none}
.facility li{font-size:13px;line-height:1.45;color:var(--muted);padding-left:22px;position:relative;margin-bottom:9px}
.facility li::before{content:"";position:absolute;left:0;top:7px;width:6px;height:6px;background:var(--olive);border-radius:50%}

.care{left:152px;top:788px;width:420px;height:432px;background:var(--olive);padding:40px 36px;color:var(--white)}
.care h3{font-family:"Montserrat",sans-serif;font-weight:700;font-size:22px;letter-spacing:1px;margin-bottom:30px}
.care ol{list-style:none;counter-reset:c}
.care li{counter-increment:c;font-size:16px;line-height:1.35;margin-bottom:18px;padding-left:44px;position:relative}
.care li::before{content:"0" counter(c);position:absolute;left:0;top:0;font-family:"Montserrat",sans-serif;font-weight:600}
.photo{position:absolute}
.p1{left:572px;top:788px;width:500px;height:432px;background:linear-gradient(160deg,#6b5a44,#3e3428 60%,#8a7a66)}
.p2{left:152px;top:1220px;width:420px;height:440px;background:linear-gradient(180deg,#c46a2e 0%,#a8572a 35%,#b9b5ac 65%,#8f8b82 100%)}
.p3{left:572px;top:1220px;width:500px;height:440px;background:linear-gradient(180deg,#4c5a3a 0%,#2f3a26 50%,#6a6a4c 100%)}
.p4{left:152px;top:1660px;width:420px;height:480px;background:linear-gradient(180deg,#8fb8e0 0%,#6f8b5a 40%,#8d8c5e 75%,#b4a880 100%)}
.p5{left:572px;top:1660px;width:500px;height:480px;background:linear-gradient(180deg,#e8eef2 0%,#7fa05a 35%,#a3352c 55%,#c6c1b2 100%)}

.options{left:152px;top:2152px;width:432px;height:336px;border:2px solid var(--olive);background:var(--white);padding:40px 34px}
.options h3{font-family:"Montserrat",sans-serif;font-weight:700;font-size:19px;line-height:1.3;color:var(--olive);letter-spacing:.5px;margin-bottom:30px}
.options ul{list-style:none}
.options li{font-size:14px;color:var(--muted);margin-bottom:16px}
.price{left:600px;top:2152px;width:472px;height:336px;background:var(--olive);border:8px solid var(--cream);outline:2px solid var(--olive);color:var(--white);padding:50px 60px;font-family:"Montserrat",sans-serif}
.price .label{font-size:14px;letter-spacing:2px;font-weight:600}
.price .amount{font-size:64px;font-weight:700;margin-top:10px;letter-spacing:1px}
.price .amount sup{font-size:26px;vertical-align:32px}
.price .amount small{font-size:30px}
.price .per{text-align:right;font-size:12px;margin-top:-8px;padding-right:40px}
.price .note{text-align:center;font-size:13px;margin-top:20px;letter-spacing:1px}

.contact-title{left:0;top:2540px;width:1200px;text-align:center;font-family:"Montserrat",sans-serif;font-weight:600;font-size:54px;color:var(--olive);letter-spacing:2px}
.field{position:absolute;height:40px;border:1.5px solid var(--olive);background:var(--white);font-size:12px;color:var(--muted);padding:12px 14px}
.f1{left:312px;top:2636px;width:248px}
.f2{left:632px;top:2636px;width:248px}
.f3{left:312px;top:2720px;width:248px}
.f4{left:632px;top:2720px;width:248px}
.f5{left:312px;top:2790px;width:568px;height:110px}
.submit{left:512px;top:2934px;width:176px;text-align:center}

.footer{left:0;top:3036px;width:1200px;height:88px;background:var(--olive);color:var(--white);text-align:center;font-family:"Montserrat",sans-serif;font-size:12px;padding-top:22px;letter-spacing:1px}
.footer .row{display:flex;justify-content:center;gap:60px;margin-bottom:10px}
.footer b{font-weight:700;margin-right:10px}
.footer .copy{font-size:10px;opacity:.9}
</style>
</head>
<body>
<header class="abs hero" role="img" aria-label="Stable aisle with a rider and horse at dusk">
</header>
<div class="abs brand"><span class="brand-dot"></span>COPPER BROOK ESTATE</div>
<nav class="abs nav">
  <a class="active" href="#">HOME</a><a href="#">ABOUT</a><a href="#">SERVICES</a><a href="#">GALLERY</a><a href="#">CURRENT EVENTS</a><a href="#">CONTACT</a>
</nav>
<h1 class="abs hero-title">COPPER BROOK<br>STABLES</h1>
<p class="abs hero-sub">Located in Southern Oregon's beautiful Willow Creek Valley</p>
<a class="abs btn hero-btn" href="#">CHECK OUR SERVICES</a>
<p class="abs hero-tag">OPEN TO TRAINERS AND BOARDING AVAILABLE NOW!</p>

<section class="abs welcome">
  <h2>WELCOMING RIDERS OF ALL DISCIPLINES AND LEVELS</h2>
  <p>OUR FACILITY INCLUDES:</p>
</section>
<div class="abs facility">
  <ul>
    <li>200x60 covered and lighted arena</li>
    <li>Trails through gorgeous meadows and forests</li>
    <li>Hot and cold water wash rack</li>
    <li>Manager lives on site</li>
    <li>Horse training also available for additional cost, specializing in dressage, barrel racing, and problem horses</li>
  </ul>
  <ul>
    <li>2 Outdoor arenas, one large and one smaller - great for warming up</li>
    <li>Large tack rooms</li>
    <li>ZELTA remote coaching in covered arena</li>
    <li>Riding lessons for various disciplines and skill levels available for additional cost</li>
    <li>All levels of riders welcome</li>
  </ul>
</div>

<section class="abs care">
  <h3>FULL CARE BOARD INCLUDES:</h3>
  <ol>
    <li>Quality grass hay fed twice a day</li>
    <li>Daily feeding of grain/supplements provided by owner</li>
    <li>Stalls/paddocks cleaned 5 days a week (box stalls cleaned daily)</li>
    <li>Shavings provided</li>
    <li>Fly masks on/off</li>
  </ol>
</section>
<div class="photo p1" role="img" aria-label="Rider leading a horse along the stable aisle"></div>
<div class="photo p2" role="img" aria-label="Covered arena with timber roof trusses and sand footing"></div>
<div class="photo p3" role="img" aria-label="Forest trail through tall pines"></div>
<div class="photo p4" role="img" aria-label="Valley view of the estate grounds and paddocks"></div>
<div class="photo p5" role="img" aria-label="Red barn with open center aisle"></div>

<section class="abs options">
  <h3>WE OFFER MULTIPLE BOARDING OPTIONS TO BEST SUIT YOUR HORSE'S NEEDS:</h3>
  <ul>
    <li>Large paddocks with run in sheds</li>
    <li>12x12 Box stalls with daily turnout (weather permitting)</li>
    <li>12x12 Stalls with large attached runs</li>
  </ul>
</section>
<section class="abs price">
  <div class="label">COST:</div>
  <div class="amount"><sup>$</sup>500<small>.00</small></div>
  <div class="per">per month</div>
  <div class="note">With multiple horse discounts available</div>
</section>

<h2 class="abs contact-title">CONTACT US</h2>
<div class="field f1">First Name</div>
<div class="field f2">Last Name</div>
<div class="field f3">Email</div>
<div class="field f4">Phone Number</div>
<div class="field f5">Message</div>
<a class="abs btn submit" href="#">SUBMIT</a>

<footer class="abs footer">
  <div class="row"><span><b>CONTACT</b>(541) 555-0148</span><span><b>EMAIL</b>hello@copperbrookestate.com</span></div>
  <div class="copy">© COPYRIGHT 2024 · ALL RIGHTS RESERVED · COPPER BROOK ESTATE</div>
</footer>
</body>
</html>
```